TriVex Business Card Design - double sided -plumbing local plumbing company

We have a Plumbing company where the design was create through Sketch Hive. We would now like a business card designed as well. We want it to be in the colour version of the logo.

Details below for the card.

Phone Number: 0438 615 247
Email: info@trivexplumbing.example.au
Website: https://trivexplumbing.example.au
We really want a sophisticated design that stand out from the other- informative and timeless.

Target Market(s)

local Canberra market

Industry/Entity Type

Plumbing, gas fitting, hot water

Contact Information for Business Card

Phone number, email, logo and "Supplying all your heating, cooling and hot water needs"

Requirements
Must have
• bust be colourful, must also be though about it being printed on a magnet. must Vex with the logo - I dont want the logo and information chucked onto a white canvas I would prefer it to be smooth and look purposeful

```html
<!DOCTYPE html>
<html lang="en">
<head>
<meta charset="utf-8">
<title>TriVex Business Card – Front and Back</title>
<link rel="stylesheet" href="https://fonts.googleapis.com/css2?family=Open+Sans:wght@400;600;700&display=swap">
<style>
  :root {
    --brand-blue: #00aeef;
    --brand-orange: #fbb040;
    --ink: #2b2b2b;
    --card: #ffffff;
    --backdrop: #e9e6e1;
  }
  * { margin: 0; padding: 0; box-sizing: border-box; }
  html, body {
    width: 1200px; height: 821px; overflow: hidden;
    background: var(--backdrop);
    font-family: "Open Sans", sans-serif;
  }
  .stage { position: relative; width: 1200px; height: 821px; }
  .card {
    position: absolute; width: 560px; height: 320px;
    background: var(--card); border-radius: 18px; overflow: hidden;
    box-shadow: 0 10px 28px rgba(0,0,0,.18);
  }
  .card--front { left: 60px; top: 70px; }
  .card--back { left: 580px; top: 430px; }

  .wordmark {
    color: var(--brand-blue); font-weight: 700; letter-spacing: 1px;
    line-height: 1;
  }
  .card--front .wordmark {
    position: absolute; left: 0; right: 0; top: 92px;
    text-align: center; font-size: 104px;
  }
  .tagline-band {
    position: absolute; left: 0; right: 0; bottom: 0; height: 48px;
    background: var(--brand-blue);
    display: flex; align-items: center; justify-content: flex-end;
    padding-right: 30px;
  }
  .tagline {
    color: #fff; font-size: 17px; font-weight: 400; letter-spacing: .3px;
  }

  .card--back .wordmark {
    position: absolute; left: 36px; top: 110px; font-size: 58px;
  }
  .divider {
    position: absolute; left: 282px; top: 70px; width: 2px; height: 130px;
    background: var(--brand-blue);
  }
  .contact-block { position: absolute; left: 306px; top: 66px; }
  .person-name {
    font-size: 22px; font-weight: 700; text-transform: uppercase; line-height: 1.1;
  }
  .person-name .first { color: var(--brand-blue); }
  .person-name .last { color: var(--brand-orange); }
  .person-role { font-size: 14px; color: var(--ink); margin-top: 2px; }
  .contact-list { list-style: none; margin-top: 16px; }
  .contact-list li {
    display: flex; align-items: center; gap: 8px;
    font-size: 12.5px; color: var(--ink); line-height: 1.75;
  }
  .contact-list svg { width: 14px; height: 14px; flex: none; }
  .wave { position: absolute; left: 0; bottom: 0; width: 560px; height: 150px; }
</style>
</head>
<body>
<main class="stage">

  <section class="card card--front" aria-label="Card front">
    <div class="wordmark">TriVex</div>
    <div class="tagline-band">
      <p class="tagline">Supplying all your heating, cooling and hot water needs</p>
    </div>
  </section>

  <section class="card card--back" aria-label="Card back">
    <div class="wordmark">TriVex</div>
    <div class="divider"></div>
    <div class="contact-block">
      <h1 class="person-name"><span class="first">Marcus</span> <span class="last">Hale</span></h1>
      <p class="person-role">Managing Director</p>
      <ul class="contact-list">
        <li>
          <svg viewBox="0 0 16 16" aria-hidden="true"><path fill="var(--brand-blue)" d="M3.6 1.5 6 1l1.2 3.3-1.6 1.1a8 8 0 0 0 5 5l1.1-1.6L15 10l-.5 2.4c-.2.9-1 1.4-1.9 1.3C6.8 13 3 9.2 2.3 3.4c-.1-.9.4-1.7 1.3-1.9Z"/></svg>
          0438 615 247
        </li>
        <li>
          <svg viewBox="0 0 16 16" aria-hidden="true"><rect x="1" y="3" width="14" height="10" rx="1.5" fill="var(--brand-orange)"/><path d="M1.5 4 8 9l6.5-5" fill="none" stroke="#fff" stroke-width="1.3"/></svg>
          info@trivexplumbing.example.au
        </li>
        <li>
          <svg viewBox="0 0 16 16" aria-hidden="true"><circle cx="8" cy="8" r="7" fill="var(--brand-orange)"/><path d="M1 8h14M8 1c-3 3.5-3 10.5 0 14M8 1c3 3.5 3 10.5 0 14" fill="none" stroke="#fff" stroke-width="1"/></svg>
          www.trivexplumbing.example.au
        </li>
      </ul>
    </div>
    <svg class="wave" viewBox="0 0 560 150" preserveAspectRatio="none" aria-hidden="true">
      <path d="M0 150 C60 95 150 90 260 95 C380 100 480 70 560 10 L560 150 Z" fill="var(--brand-orange)"/>
      <path d="M0 150 C65 104 155 100 262 104 C382 108 484 80 560 24 L560 150 Z" fill="#fff"/>
      <path d="M0 150 C70 112 160 108 264 111 C386 114 488 88 560 34 L560 150 Z" fill="var(--brand-blue)"/>
    </svg>
  </section>

</main>
</body>
</html>
```